Business Card Design Project

A new design for our business cards for a small casting/talent agency, we would like to incorporate the logo and brand colors within the design, below are the information that should be on the card

(Name)
(Title)

Corvane Reels FZ-LLC
Harlow Studio Park
Building 7, Suite 418
Dubai, UAE
PO Box 681247
+97143810579
info@CorvaneReels.com

Target Market(s)

production companies, film makers, media, entertainment industry

Industry/Entity Type

Business

Requirements
Must have
• logo, logo colors
Nice to have
• cutting edge design, sleek and modern
Should not have
• playful, funky, congested

```html
<!DOCTYPE html>
<html lang="en">
<head>
<meta charset="utf-8">
<title>Corvane Reels — Business Card</title>
<link rel="stylesheet" href="https://fonts.googleapis.com/css2?family=Montserrat:wght@700&family=Questrial&display=swap">
<style>
  :root {
    --backdrop: #141416;
    --navy: #0f2f6e;
    --navy-deep: #0a2052;
    --navy-light: #173d86;
    --card-white: #ffffff;
    --mist: #d9dde2;
    --ink-grey: #5a5d63;
    --logo-grey: #c9ced6;
    --on-navy: #ffffff;
  }
  * { box-sizing: border-box; margin: 0; padding: 0; }
  html, body { width: 1200px; height: 675px; overflow: hidden; }
  body {
    background: var(--backdrop);
    display: flex;
    align-items: center;
    justify-content: center;
    gap: 60px;
    font-family: "Questrial", "Century Gothic", sans-serif;
  }
  .card {
    position: relative;
    width: 520px;
    height: 297px;
    overflow: hidden;
    border-radius: 2px;
    box-shadow: 0 12px 30px rgba(0,0,0,.55);
  }

  /* Front */
  .card--front { background: var(--card-white); }
  .front__mark {
    position: absolute;
    left: -150px;
    top: -20px;
    width: 400px;
    height: 400px;
    border-radius: 50%;
    background: var(--mist);
  }
  .front__details {
    position: absolute;
    left: 268px;
    top: 78px;
    color: var(--ink-grey);
  }
  .holder__name {
    font-family: "Montserrat", "Century Gothic", sans-serif;
    font-weight: 700;
    font-size: 24px;
    color: var(--navy);
    letter-spacing: .2px;
    line-height: 1;
  }
  .holder__title { font-size: 10px; margin-top: 4px; }
  .company {
    margin-top: 20px;
    font-size: 10.5px;
    line-height: 1.35;
  }
  .company__name { font-weight: 700; color: var(--navy); font-family: "Montserrat", sans-serif; font-size: 10px; }
  .contact { margin-top: 14px; list-style: none; font-size: 10.5px; line-height: 1.55; }
  .contact__item { display: flex; align-items: center; gap: 7px; }
  .contact__icon { width: 10px; height: 10px; fill: var(--navy); flex: none; }

  /* Back */
  .card--back {
    background: radial-gradient(ellipse at 30% 40%, var(--navy-light), var(--navy) 55%, var(--navy-deep));
  }
  .back__site {
    position: absolute;
    right: 34px;
    top: 30px;
    font-size: 10px;
    color: var(--on-navy);
    letter-spacing: .3px;
  }
  .brand {
    position: absolute;
    left: 110px;
    top: 78px;
    width: 150px;
    height: 150px;
    border-radius: 50%;
    border: 2px solid var(--logo-grey);
    display: flex;
    align-items: center;
    justify-content: center;
    text-align: center;
  }
  .brand__name {
    font-size: 24px;
    line-height: 1.05;
    color: var(--on-navy);
  }
</style>
</head>
<body>

  <section class="card card--front" aria-label="Business card front">
    <div class="front__mark" role="img" aria-label="Large faint brand mark decoration"></div>
    <div class="front__details">
      <h1 class="holder__name">Elias Marlow</h1>
      <p class="holder__title">President &amp; CEO</p>
      <p class="company">
        <span class="company__name">Corvane Reels FZ-LLC</span><br>
        Harlow Studio Park, Building 7, Suite 418<br>
        Dubai, UAE, PO Box 681247
      </p>
      <ul class="contact">
        <li class="contact__item">
          <svg class="contact__icon" viewBox="0 0 10 10" aria-hidden="true"><path d="M1 3.5C1 2 2 1.5 5 1.5S9 2 9 3.5L7.5 4V3.2H2.5V4ZM2 5h6l1 3.5H1Z"/></svg>
          +97143810579
        </li>
        <li class="contact__item">
          <svg class="contact__icon" viewBox="0 0 10 10" aria-hidden="true"><path d="M0.5 2h9v6h-9Z M1 2.6 5 5.6 9 2.6" stroke="#fff" stroke-width=".8"/></svg>
          info@CorvaneReels.com
        </li>
      </ul>
    </div>
  </section>

  <section class="card card--back" aria-label="Business card back">
    <p class="back__site">www.CorvaneReels.com</p>
    <div class="brand">
      <span class="brand__name">Corvane<br>Reels</span>
    </div>
  </section>

</body>
</html>
```